Real Estate Biz Card

-Card Size: Standard
-Background: Dark grey or black. I am open to gradient or a textured background.
-Other Colors: I dont mind pops of color. Contrasty blue, lime green, red Etc. Feel free to get creative.
-Text color: be creative
-Font: I like modern styles. Something that works well with my KV718 logo. See attached
-I would like my logo (KV718) watermarked on the card. Either on one side or both.
-Front of Card: keep it simple. Head shot, name, Logo, Phone #
-Back: add the rest of the details. See list below.
-brokerages logo as well as the Dwellon and Equal Housing Opportunity logos on the card
-Name: Milo Dravek
-Residential Real Estate
-Cell:
-Email:
-Site:
-Office Address:
-very small/fine print "Each office independently owned & operated

```html
<!DOCTYPE html>
<html lang="en">
<head>
<meta charset="utf-8">
<title>KV718 Business Card</title>
<link href="https://fonts.googleapis.com/css2?family=Open+Sans:wght@400;600&display=swap" rel="stylesheet">
<style>
  :root {
    --stage: #3a3a3a;
    --card: #1f1f20;
    --card-edge: #2a2a2b;
    --white: #f2f2f2;
    --muted: #9a9a9a;
    --faint: rgba(255,255,255,0.05);
    --band: #8a8a8a;
    --shirt: #4f6a9a;
  }
  * { box-sizing: border-box; margin: 0; padding: 0; }
  html, body { width: 1200px; height: 716px; overflow: hidden; }
  body {
    background: var(--stage);
    font-family: "Open Sans", sans-serif;
    color: var(--white);
    position: relative;
  }
  .card {
    position: absolute;
    top: 203px;
    width: 540px;
    height: 310px;
    border-radius: 18px;
    background: linear-gradient(160deg, var(--card-edge), var(--card));
    overflow: hidden;
  }
  .card--back { left: 40px; }
  .card--front { left: 620px; }

  .brand { position: absolute; display: flex; flex-direction: column; }
  .brand__row { display: flex; align-items: center; gap: 10px; }
  .brand__name {
    font-family: "Open Sans", sans-serif;
    font-weight: 600;
    color: var(--white);
    letter-spacing: 1px;
    line-height: 1;
  }
  .brand__mark { width: 12px; height: 12px; background: var(--white); }
  .brand__line {
    font-size: 11px;
    color: var(--muted);
    margin-top: 6px;
  }

  /* back */
  .card--back .brand { left: 150px; top: 30px; }
  .card--back .brand__name { font-size: 48px; }
  .contact { position: absolute; left: 40px; top: 118px; list-style: none; }
  .contact li {
    display: flex; align-items: center; gap: 10px;
    font-size: 12px; color: var(--muted); margin-bottom: 9px; line-height: 16px;
  }
  .contact svg { width: 11px; height: 11px; fill: var(--muted); }
  .website { position: absolute; left: 40px; top: 206px; font-size: 12px; color: var(--muted); }
  .rule { position: absolute; left: 20px; top: 232px; width: 320px; height: 2px; background: var(--muted); opacity: .6; }
  .social-note { position: absolute; left: 372px; top: 212px; font-size: 10px; color: var(--white); }
  .social { position: absolute; left: 348px; top: 230px; display: flex; gap: 8px; }
  .social span { width: 14px; height: 14px; background: var(--muted); border-radius: 2px; }
  .badges { position: absolute; right: 44px; top: 96px; display: flex; gap: 12px; align-items: flex-end; }
  .badge { display: flex; flex-direction: column; align-items: center; gap: 4px; }
  .badge__shape { width: 38px; height: 38px; border: 2px solid var(--white); }
  .badge__shape--house { width: 44px; height: 34px; border-radius: 4px; margin-bottom: 14px; }
  .badge__label { font-size: 7px; color: var(--muted); letter-spacing: 1px; text-transform: uppercase; }
  .brokerage { position: absolute; right: 44px; top: 160px; }
  .brokerage__name { font-size: 17px; font-weight: 600; color: var(--white); line-height: 1.1; }
  .brokerage__sub { font-size: 9px; color: var(--muted); letter-spacing: 1px; }

  /* front */
  .watermark {
    position: absolute; left: 24px; top: 60px;
    font-weight: 600;
    font-size: 140px; color: var(--faint); letter-spacing: 2px; line-height: 1;
  }
  .card--front .brand { left: 120px; top: 40px; }
  .card--front .brand__name { font-size: 52px; }
  .identity { position: absolute; left: 0; top: 170px; }
  .identity__line { display: flex; align-items: baseline; gap: 12px; padding-left: 36px; }
  .identity__name { font-size: 18px; font-weight: 600; letter-spacing: 1px; text-transform: uppercase; }
  .identity__phone { font-size: 15px; }
  .identity__band {
    margin-top: 6px; width: 320px; height: 24px; background: var(--band);
    padding-left: 36px; font-size: 12px; line-height: 24px; color: var(--card);
  }
  .headshot {
    position: absolute; right: 0; bottom: 0; width: 220px; height: 190px;
    background: linear-gradient(180deg, #2a2a2a 0%, #3c3f46 45%, var(--shirt) 100%);
  }
</style>
</head>
<body>
  <section class="card card--back">
    <div class="brand">
      <div class="brand__row"><span class="brand__name">KV718</span><span class="brand__mark"></span></div>
      <span class="brand__line">Residential Homes</span>
    </div>
    <ul class="contact">
      <li><svg viewBox="0 0 10 10"><path d="M5 0a3.5 3.5 0 0 0-3.5 3.5C1.5 6 5 10 5 10s3.5-4 3.5-6.5A3.5 3.5 0 0 0 5 0zm0 5a1.5 1.5 0 1 1 0-3 1.5 1.5 0 0 1 0 3z"/></svg>Your address</li>
      <li><svg viewBox="0 0 10 10"><rect x="2.5" y="0" width="5" height="10" rx="1"/></svg>000 000 0000</li>
      <li><svg viewBox="0 0 10 10"><rect x="0" y="2" width="10" height="6" rx="1"/></svg>youremail@xyz.com</li>
    </ul>
    <div class="website">www.yourwebsite.com</div>
    <div class="rule"></div>
    <div class="social-note">(if needed)</div>
    <div class="social"><span></span><span></span><span></span><span></span><span></span><span></span></div>
    <div class="badges">
      <div class="badge"><span class="badge__shape"></span><span class="badge__label">Dwellon</span></div>
      <div class="badge"><span class="badge__shape badge__shape--house"></span></div>
    </div>
    <div class="brokerage">
      <div class="brokerage__name">Harbor Key Eastside</div>
      <div class="brokerage__sub">HARBOR KEY</div>
    </div>
  </section>

  <section class="card card--front">
    <div class="watermark" aria-hidden="true">KV718</div>
    <div class="brand">
      <div class="brand__row"><span class="brand__name">KV718</span><span class="brand__mark"></span></div>
      <span class="brand__line">Residential Homes</span>
    </div>
    <div class="identity">
      <div class="identity__line">
        <span class="identity__name">Milo Dravek</span>
        <span class="identity__phone">555.014.2290</span>
      </div>
      <div class="identity__band">Real Estate Broker</div>
    </div>
    <div class="headshot" role="img" aria-label="Headshot of the broker in a blue shirt"></div>
  </section>
</body>
</html>
```